Redesign retirement planner website

Provide an original design for a website. The site should introduce the retirement planner, explain the basic offerings of his services, and invite the website visitor to enter their name, phone, and email. Please provide a ready-to-publish redesign that can actually be published via a Wordpress template or other major website builder like SquareSpace or Wix. Some introductory content is attached, but feel free to add additional sections/images/blocks/copywriting and rearrange/delete sections entirely to make your design original and compelling. Feel free to pull copywriting from here but again, do not use this original design, feel free to create an entirely NEW design and layout. tern-melon-zobr (dot) sitelarkhost (dot) com password: 1234 -- FINAL NOTE: Do not choose a stock photo of a man for the retirement planner. This website needs to work well with no photo of the retirement planner himself. Think of a non-face-focused design to win this competition.

Industry/Entity Type

Retirement planner personal website

Number of Pages Required

1 page

Font styles to use
Sans Serif
Decorative

Requirements
Must have
• Please provide a ready-to-publish redesign that can actually be published via a Wordpress template or other major website builder.

```html
<!DOCTYPE html>
<html lang="en">
<head>
<meta charset="utf-8">
<title>Darren Wexley — Counselor &amp; Retirement Specialist</title>
<link href="https://fonts.googleapis.com/css2?family=Courgette&family=Poppins:wght@600;700&family=Work+Sans:wght@400;500;600&display=swap" rel="stylesheet">
<style>
:root{
  --gold:#ffc700;
  --ink:#0a0a0a;
  --panel:#141414;
  --dark:#1c1c1c;
  --pattern:#262626;
  --white:#ffffff;
  --muted:#c9c9c9;
  --field:#2a2a2a;
}
*{box-sizing:border-box;margin:0;padding:0}
html,body{width:1200px;height:4248px;overflow:hidden;background:var(--ink)}
body{position:relative;font-family:"Work Sans",Arial,sans-serif;color:var(--white)}
.script{font-family:"Courgette",cursive;font-weight:400}
section,header{position:absolute;left:0;width:1200px;overflow:hidden}
.fill{position:absolute;inset:0}
.btn{display:inline-block;background:var(--gold);color:var(--ink);font-weight:600;font-size:17px;padding:12px 22px;border-radius:4px}

/* hero */
.hero{top:0;height:700px}
.hero .fill{background:radial-gradient(ellipse at 50% 40%,#6a6f75 0%,#3c3f44 45%,#17181a 100%)}
.nav{position:absolute;top:26px;left:64px;right:64px;display:flex;justify-content:space-between;align-items:center}
.logo{font-family:"Courgette",cursive;color:var(--gold);font-size:30px}
.nav ul{list-style:none;display:flex;gap:64px;font-size:17px;font-weight:500}
.nav li.active{border-bottom:2px solid var(--gold);padding-bottom:4px}
.hero-text{position:absolute;top:330px;width:100%;text-align:center}
.hero-text .lead{font-size:32px}
.hero-text h1{font-family:"Poppins",sans-serif;color:var(--gold);font-size:66px;line-height:84px;font-weight:700;margin-top:6px}
.hero-text .tag{font-size:34px;margin-top:8px}

/* about */
.about{top:700px;height:568px;background:var(--ink)}
.about .photo{position:absolute;left:0;top:0;width:600px;height:568px;background:linear-gradient(135deg,#c9b9a2 0%,#8a6b4c 45%,#3b2b1f 100%)}
.about .copy{position:absolute;left:668px;top:120px;width:470px}
.about h2{color:var(--gold);font-size:44px;margin-bottom:26px}
.about p{font-size:17px;line-height:27px;margin-bottom:30px}

/* specialties */
.specialties{top:1268px;height:992px;background:var(--pattern)}
.sec-title{position:absolute;width:100%;text-align:center;color:var(--gold);font-size:46px}
.spec{position:absolute;width:300px;text-align:center}
.spec .icon{width:110px;height:110px;border-radius:50%;background:var(--gold);margin:0 auto 22px;display:flex;align-items:center;justify-content:center}
.spec h3{font-size:21px;font-weight:600;margin-bottom:12px}
.spec p{font-size:14px;line-height:21px;color:var(--muted)}
.spec.featured{background:#161616;padding:40px 22px;width:340px}
.spec.featured h3{color:var(--gold);text-decoration:underline}

/* testimonials */
.testimonials{top:2260px;height:720px;background:#0e0e0e}
.quote{position:absolute;top:252px;width:480px;height:250px;background:var(--dark);padding:100px 32px 0}
.avatar{position:absolute;top:-30px;left:48px;width:104px;height:104px;border-radius:50%;background:linear-gradient(#bdbdbd,#6f6f6f);border:4px solid #e5e5e5}
.quote p{font-size:15px;line-height:22px;color:var(--muted)}
.quote .who{display:flex;justify-content:space-between;margin-top:18px;font-weight:600;font-size:17px}
.stars{color:var(--gold);letter-spacing:3px}
.dots{position:absolute;top:524px;left:554px;display:flex;gap:20px}
.dots span{width:36px;height:36px;border-radius:50%;background:#555}
.dots span.on{background:var(--gold)}

/* insurance */
.insurance{top:2980px;height:560px;background:var(--pattern)}
.ins{position:absolute;top:124px;width:340px;height:360px;overflow:hidden}
.ins .img{position:absolute;inset:0}
.ins h3{position:absolute;bottom:26px;left:0;right:0;text-align:center;font-size:23px;font-weight:600;line-height:30px}
.ins.mid{background:linear-gradient(#3a3318,#231e0c);text-align:center;padding:76px 30px 0}
.ins.mid h3{position:static;margin-bottom:16px}
.ins.mid p{font-size:15px;line-height:21px;color:var(--muted);margin-bottom:20px}
.ins.mid .more{display:inline-block;background:#111;color:var(--white);font-size:14px;font-weight:600;padding:10px 18px}

/* contact */
.contact{top:3540px;height:708px}
.contact .fill{background:linear-gradient(180deg,#4a4f55 0%,#2a2d31 55%,#141516 100%)}
.contact h2{position:absolute;left:72px;top:86px;color:var(--gold);font-size:44px}
.contact .sub{position:absolute;left:72px;top:164px;font-size:22px;font-weight:600}
.info{position:absolute;left:72px;width:520px;display:flex;align-items:center;gap:22px}
.info .ic{width:40px;height:40px;border-radius:50%;background:var(--gold);display:flex;align-items:center;justify-content:center;flex:none}
.info small{display:block;font-size:13px;color:var(--muted)}
.info span{font-size:15px;font-weight:500}
.form{position:absolute;left:640px;top:222px;width:488px}
.field{height:52px;background:var(--field);border:1px solid #555;padding:0 16px;display:flex;align-items:center;font-size:15px;color:#ddd;margin-bottom:28px}
.row{display:flex;gap:20px}
.row .field{flex:1}
.signup{display:flex;justify-content:space-between;align-items:center;margin-top:4px}
.signup label{display:flex;align-items:center;gap:14px;font-size:15px}
.signup .box{width:20px;height:20px;border:2px solid var(--white)}
.foot{position:absolute;bottom:0;width:100%;height:108px;text-align:center;font-size:14px}
.foot p{margin-top:34px;color:var(--muted)}
.foot ul{list-style:none;display:flex;justify-content:center;gap:18px;margin-top:18px;color:var(--gold)}
</style>
</head>
<body>

<header class="hero">
  <div class="fill" role="img" aria-label="Upward view of city skyscrapers against the sky"></div>
  <nav class="nav">
    <div class="logo">Darren Wexley</div>
    <ul><li class="active">Home</li><li>Specialties</li><li>Testimonials</li><li>Contact Me</li></ul>
  </nav>
  <div class="hero-text">
    <div class="lead script">I'm a</div>
    <h1>Counselor &amp;<br>Retirement Specialist</h1>
    <div class="tag script">with a unique approach to financial planning</div>
  </div>
</header>

<section class="about">
  <div class="photo" role="img" aria-label="Older couple's hands held together on a wooden table"></div>
  <div class="copy">
    <h2 class="script">About Me</h2>
    <p>You have a lifetime of accomplishments. Learning about them is my extraordinary honor. When I meet clients to make a plan for their final years of work and savings, I understand my solemn privilege. Your capital is irreplaceable. My job is to maximize its benefit for your health, family, and legacy.</p>
    <span class="btn">Contact Me</span>
  </div>
</section>

<section class="specialties">
  <h2 class="sec-title script" style="top:84px">My Specialties</h2>

  <div class="spec" style="left:190px;top:216px">
    <div class="icon"><svg width="56" height="56" viewBox="0 0 56 56" fill="none" stroke="#0a0a0a" stroke-width="3"><path d="M10 30 L28 14 L46 30"/><rect x="16" y="28" width="24" height="18"/></svg></div>
    <h3>Estate Planning</h3>
    <p>Ensure your legacy is protected with comprehensive estate planning. I will guide you through creating wills, trusts, and other essential documents to secure your assets for future generations, ensuring your wishes are honored.</p>
  </div>
  <div class="spec" style="left:710px;top:216px">
    <div class="icon"><svg width="56" height="56" viewBox="0 0 56 56" fill="none" stroke="#0a0a0a" stroke-width="3"><rect x="10" y="10" width="36" height="36"/><path d="M16 38 L26 28 L32 34 L42 20"/></svg></div>
    <h3>Retirement Forecasting</h3>
    <p>Plan for a fulfilling retirement with our expert forecasting services. I will analyze your financial situation and future needs to develop a personalized strategy, helping you achieve your retirement goals with confidence.</p>
  </div>

  <div class="spec" style="left:110px;top:548px">
    <div class="icon"><svg width="56" height="56" viewBox="0 0 56 56" fill="none" stroke="#0a0a0a" stroke-width="3"><rect x="14" y="8" width="28" height="40"/><path d="M20 18h16M20 26h16M20 34h10"/></svg></div>
    <h3>Final Expense</h3>
    <p>Prepare for life's final expenses with peace of mind. My services help you plan for costs associated with end-of-life arrangements, alleviating financial stress for your loved ones during a difficult time.</p>
  </div>
  <div class="spec" style="left:450px;top:548px">
    <div class="icon"><svg width="56" height="56" viewBox="0 0 56 56" fill="none" stroke="#0a0a0a" stroke-width="3"><path d="M8 28 A20 20 0 0 1 48 28 Z"/><path d="M28 28 V44 A4 4 0 0 1 20 44"/></svg></div>
    <h3>Life Insurance</h3>
    <p>Safeguard your family's future with tailored life insurance solutions. I provide expert advice to help you choose the right coverage, ensuring financial security for your loved ones when they need it most.</p>
  </div>
  <div class="spec featured" style="left:772px;top:524px">
    <div class="icon"><svg width="56" height="56" viewBox="0 0 56 56" fill="none" stroke="#0a0a0a" stroke-width="3"><circle cx="28" cy="28" r="18"/><path d="M28 18v20M22 23h9a4 4 0 0 1 0 8h-6a4 4 0 0 0 0 8h9"/></svg></div>
    <h3>Portfolio Evaluation</h3>
    <p>Maximize your investment potential with our thorough portfolio evaluation. I assess your current assets and provide strategic recommendations to enhance your financial growth and stability.</p>
  </div>
</section>

<section class="testimonials">
  <h2 class="sec-title script" style="top:96px">My Happy Clients</h2>
  <div class="quote" style="left:80px">
    <div class="avatar" role="img" aria-label="Client portrait"></div>
    <p>Temporibus autem quibusdam et aut officiis debitis aut rerum necessitatibus saepe eveniet ut et voluptates repudiandae sint et molestiae non recusandae.</p>
    <div class="who"><span>Marisol Quen</span><span class="stars">★★★★★</span></div>
  </div>
  <div class="quote" style="left:640px">
    <div class="avatar" role="img" aria-label="Client portrait"></div>
    <p>Temporibus autem quibusdam et aut officiis debitis aut rerum necessitatibus saepe eveniet ut et voluptates repudiandae sint et molestiae non recusandae.</p>
    <div class="who"><span>Tobias Renn</span><span class="stars">★★★★★</span></div>
  </div>
  <div class="dots"><span></span><span class="on"></span></div>
</section>

<section class="insurance">
  <h2 class="sec-title script" style="top:24px">Insurance Offerings</h2>
  <div class="ins" style="left:72px">
    <div class="img" role="img" aria-label="Family silhouettes forming a heart at sunset" style="background:linear-gradient(180deg,#c9a46b 0%,#8c5a2a 55%,#1f140b 100%)"></div>
    <h3>Whole and Universal<br>Life Insurance</h3>
  </div>
  <div class="ins mid" style="left:432px">
    <h3>Fixed Indexed<br>Annuities</h3>
    <p>Excellent financial vehicles for preserving and protecting capital investments.</p>
    <span class="more">Learn More</span>
  </div>
  <div class="ins" style="left:792px">
    <div class="img" role="img" aria-label="Red rose beside a photo frame and ribbon on a dark table" style="background:linear-gradient(160deg,#6b1a1a 0%,#3a3a3a 45%,#111 100%)"></div>
    <h3>Term and Final<br>Expense</h3>
  </div>
</section>

<section class="contact">
  <div class="fill" role="img" aria-label="City skyline of high-rise buildings"></div>
  <h2 class="script">Contact Me</h2>
  <div class="sub">Let's plan for golden memories</div>

  <div class="info" style="top:228px"><div class="ic"><svg width="20" height="20" viewBox="0 0 20 20" fill="none" stroke="#0a0a0a" stroke-width="2"><rect x="2" y="4" width="16" height="12"/><path d="M2 4l8 7 8-7"/></svg></div><div><small>Email</small><span>hello@wexleyplanning.example</span></div></div>
  <div class="info" style="top:320px"><div class="ic"><svg width="20" height="20" viewBox="0 0 20 20" fill="#0a0a0a"><path d="M4 2h4l2 5-3 2a11 11 0 0 0 4 4l2-3 5 2v4a2 2 0 0 1-2 2A16 16 0 0 1 2 4a2 2 0 0 1 2-2z"/></svg></div><div><small>Phone</small><span>(555) 010-2244</span></div></div>
  <div class="info" style="top:408px"><div class="ic"></div><div><small>Profile</small><span>https://profiles.example/darren-wexley</span></div></div>
  <div class="info" style="top:500px"><div class="ic"></div><div><small>Social</small><span>https://social.example/@darren.wexley</span></div></div>

  <div class="form">
    <div class="row"><div class="field">First Name *</div><div class="field">Last Name *</div></div>
    <div class="field">Email *</div>
    <div class="field">Phone</div>
    <div class="signup"><label><span class="box"></span>Sign up for news and updates</label><span class="btn">Say Hi!</span></div>
  </div>

  <div class="foot">
    <p>© 2024 Darren Wexley. All rights reserved.</p>
    <ul><li>Home</li><li>•</li><li>Specialties</li><li>•</li><li>Testimonials</li><li>•</li><li>Contact Me</li></ul>
  </div>
</section>

</body>
</html>
```